Website Design for Camp 3874

We need a website design for a new company that strives to provide training and structure for religious missionaries who are traveling the world to teach of christianity.
They provide training in:
- Nutrition Coaching & Daily assignments
- Personal Training Sessions
- Phycological emotional/mental component
The goal of Camp 3874 is to help missionaries preach the gospel of christ to those who haven't heard it due to geographical obstacles and physical limitations that get in the way.
The homepage template has linked images to use. If any other images are needed, stock images are acceptable.

Logo/Color Scheme: https://files.nervalo.example/folders/8Kp2QwZr7LmXv4TsN9bHc3YdJ6fGaE1Ru?share=open

Customer Avatar/Core Message Canvas: https://sheets.nervalo.example/s/d/7Hq39TbWmuKpZr2LxNcV8yEs5DfGa4JkQo1BnXtYRMwP/edit?share=open

Homepage Template: https://pages.nervalo.example/doc/d/5nRZ82kLp94QsWxTy7mBuVhCe3DjFa6Go0PiKqNr4Ytw/edit?share=open

```html
<!DOCTYPE html>
<html lang="en">
<head>
<meta charset="UTF-8">
<title>Camp 3874 — Missionary Training</title>
<link rel="stylesheet" href="https://fonts.googleapis.com/css2?family=Poppins:wght@300;400;500;600;700&display=swap">
<style>
:root{
  --olive:#2c3319;
  --gold:#e3b94a;
  --gold-dark:#c99d2e;
  --cream:#fdf3d6;
  --paper:#ececec;
  --ink:#2a2a22;
  --muted:#55584a;
  --white:#ffffff;
}
*{box-sizing:border-box;margin:0;padding:0}
html,body{width:1200px;height:4942px;overflow:hidden}
body{font-family:'Poppins',sans-serif;color:var(--ink);background:var(--white)}
section,header,footer{position:relative;width:1200px;overflow:hidden}
.abs{position:absolute}
.btn{display:inline-flex;align-items:center;justify-content:center;border-radius:40px;font-weight:500;font-size:20px;text-decoration:none}
.btn-gold{background:var(--gold);color:var(--olive)}
.btn-white{background:var(--white);color:var(--olive)}
.btn-olive{background:var(--olive);color:var(--gold);border-radius:10px}

/* header */
.site-header{height:131px;background:var(--white)}
.brand{left:85px;top:40px}
.brand-name{font-weight:700;font-size:42px;line-height:50px;color:var(--olive);letter-spacing:1px}
.nav{right:85px;top:50px;display:flex;align-items:center;gap:34px;font-size:15px;color:var(--muted)}
.signup{background:var(--gold);color:var(--white);border-radius:20px;padding:8px 22px;display:flex;align-items:center;gap:10px;font-size:14px}
.signup i{width:14px;height:14px;border-radius:50%;background:var(--white);display:block}

/* hero */
.hero{height:579px}
.hero-photo{inset:0;background:linear-gradient(160deg,#9fb0b8 0%,#7d8a83 30%,#5d5f4e 55%,#7a6a55 75%,#4c4a3c 100%)}
.hero-shade{inset:0;background:rgba(30,30,20,.28)}
.hero-copy{left:0;right:0;top:112px;text-align:center;color:var(--white)}
.hero-copy h1{font-size:41px;font-weight:600;line-height:52px}
.hero-copy p{margin-top:20px;font-size:19px;font-weight:300;line-height:31px}
.hero-actions{left:0;right:0;top:350px;display:flex;justify-content:center;gap:22px}
.hero-actions .btn{height:68px;padding:0 30px}
.dots{left:0;right:0;top:472px;display:flex;justify-content:center;gap:8px}
.dots i{width:12px;height:12px;border-radius:50%;background:rgba(255,255,255,.5);display:block}
.dots i:first-child{background:var(--white)}

/* staff */
.staff{height:734px}
.section-title{left:0;right:0;text-align:center;font-size:32px;font-weight:600;color:var(--olive);line-height:42px}
.staff-grid{left:114px;top:240px;width:972px;display:grid;grid-template-columns:repeat(4,240px);row-gap:40px}
.staff-item{text-align:center}
.staff-item svg{width:146px;height:146px;display:block;margin:0 auto}
.staff-item span{display:block;margin-top:20px;font-size:20px;color:var(--ink)}

/* barriers */
.barriers{height:562px;background:var(--olive)}
.barriers h2{left:85px;top:200px;font-size:32px;line-height:42px;font-weight:700;color:var(--gold)}
.divider-v{left:407px;top:102px;height:260px;border-left:2px dotted var(--gold-dark)}
.barriers-text{left:457px;top:92px;width:658px;color:var(--white);font-size:15px;line-height:26px}
.barriers-text p+p{margin-top:24px}
.barriers-text .cite{text-align:right;margin-top:14px}
.barriers .btn{left:457px;top:440px;width:232px;height:64px;border-radius:10px}

/* approach */
.approach{height:1116px}
.legend{left:0;right:0;top:166px;display:flex;justify-content:center;gap:66px;font-size:21px}
.legend span{display:flex;align-items:center;gap:14px}
.legend i{width:16px;height:16px;border-radius:50%;background:var(--gold);display:block}
.pillar{height:200px}
.pillar-band{background:var(--cream);height:200px;top:0}
.pillar svg{position:absolute;width:182px;height:182px;top:9px}
.pillar h3{position:absolute;font-size:26px;font-weight:500;color:var(--ink);top:42px}
.pillar p{position:absolute;font-size:15px;line-height:26px;color:var(--muted);top:96px}
.approach .btn{left:380px;top:1005px;width:440px;height:82px}

/* audience */
.audience{height:1160px;background:var(--olive)}
.audience h2{left:127px;top:180px;font-size:64px;line-height:84px;font-weight:600;color:var(--white)}
.card{background:var(--paper);border-radius:8px;width:498px;height:345px;text-align:center;padding:0 22px}
.card h3{margin-top:110px;font-size:20px;font-weight:600;color:var(--olive);white-space:nowrap}
.card p{margin-top:16px;font-size:15px;line-height:26px;color:var(--muted)}
.card-hex{width:134px;height:134px}
.audience .btn{left:442px;top:995px;width:316px;height:72px;border-radius:10px}

/* newsletter */
.newsletter{height:457px;background:#efefef}
.newsletter h2{left:0;right:0;top:78px;text-align:center;font-size:32px;line-height:38px;font-weight:600;color:var(--olive)}
.newsletter p{left:0;right:0;top:218px;text-align:center;font-size:15px;line-height:26px;color:var(--ink)}
.signup-form{left:276px;top:296px;width:648px;height:72px;background:var(--white);border-radius:40px;display:flex;align-items:center;justify-content:space-between}
.signup-form span{padding-left:40px;font-size:15px;color:#888}
.signup-form b{background:var(--olive);color:var(--white);font-weight:400;font-size:28px;height:72px;width:196px;border-radius:40px;display:flex;align-items:center;justify-content:center}

/* footer */
.site-footer{height:203px;background:var(--olive);color:var(--white)}
.foot-brand{left:97px;top:56px}
.foot-brand .brand-name{color:var(--white);font-size:40px;line-height:48px}
.foot-info{display:flex;align-items:center;gap:16px;font-size:15px;line-height:20px}
.foot-info i{width:36px;height:36px;border-radius:50%;background:var(--gold);display:flex;align-items:center;justify-content:center}
.socials{right:106px;top:68px;display:flex;gap:8px}
.socials i{width:30px;height:30px;border-radius:50%;border:2px solid var(--gold);display:block}
.foot-rule{left:85px;right:85px;top:148px;border-top:1px solid rgba(255,255,255,.25)}
.copy{left:85px;top:168px;font-size:13px}
.legal{right:85px;top:168px;font-size:13px}
.legal a{color:var(--white);text-decoration:none}
.legal a.active{color:var(--gold)}
</style>
</head>
<body>

<header class="site-header">
  <div class="abs brand"><span class="brand-name">CAMP 3874</span></div>
  <nav class="abs nav">
    <span>Programs</span><span>Events</span><span>Online Store</span><span>About Us</span><span>Contact Us</span>
    <span class="signup"><i></i>Sign-up</span>
  </nav>
</header>

<section class="hero">
  <div class="abs hero-photo" role="img" aria-label="Photograph of a rugged mountain range under a hazy sky"></div>
  <div class="abs hero-shade"></div>
  <div class="abs hero-copy">
    <h1>“Empowing Change: By Illuminating<br>Lives Unexposed to The Gospel’s Light”</h1>
    <p>Camp 3874’s mission is to enable the word of Jesus to be experienced<br>by people in the most remote and treacherous parts of the world</p>
  </div>
  <div class="abs hero-actions">
    <a class="btn btn-white">View Our Programs</a>
    <a class="btn btn-gold">Register for Training</a>
  </div>
  <div class="abs dots"><i></i><i></i><i></i><i></i></div>
</section>

<section class="staff">
  <h2 class="abs section-title" style="top:82px">Camp 3874’s Well-Rounded Staff<br>for Specialized Training</h2>
  <div class="abs staff-grid">
    <div class="staff-item"><svg viewBox="0 0 100 100" role="img" aria-label="Pastor icon"><polygon points="30,0 70,0 100,30 100,70 70,100 30,100 0,70 0,30" fill="#e3b94a"/><circle cx="50" cy="50" r="34" fill="#2c3319"/></svg><span>Pastor</span></div>
    <div class="staff-item"><svg viewBox="0 0 100 100" role="img" aria-label="Nutritionist icon"><polygon points="30,0 70,0 100,30 100,70 70,100 30,100 0,70 0,30" fill="#e3b94a"/><circle cx="50" cy="50" r="34" fill="#2c3319"/></svg><span>Nutritionist</span></div>
    <div class="staff-item"><svg viewBox="0 0 100 100" role="img" aria-label="Dietician icon"><polygon points="30,0 70,0 100,30 100,70 70,100 30,100 0,70 0,30" fill="#e3b94a"/><circle cx="50" cy="50" r="34" fill="#2c3319"/></svg><span>Dietician</span></div>
    <div class="staff-item"><svg viewBox="0 0 100 100" role="img" aria-label="Professional trainer icon"><polygon points="30,0 70,0 100,30 100,70 70,100 30,100 0,70 0,30" fill="#e3b94a"/><circle cx="50" cy="50" r="34" fill="#2c3319"/></svg><span>Professional Trainer</span></div>
    <div class="staff-item"><svg viewBox="0 0 100 100" role="img" aria-label="Former ranger icon"><polygon points="30,0 70,0 100,30 100,70 70,100 30,100 0,70 0,30" fill="#e3b94a"/><circle cx="50" cy="50" r="34" fill="#2c3319"/></svg><span>Former Ranger</span></div>
    <div class="staff-item"><svg viewBox="0 0 100 100" role="img" aria-label="Former special ops icon"><polygon points="30,0 70,0 100,30 100,70 70,100 30,100 0,70 0,30" fill="#e3b94a"/><circle cx="50" cy="50" r="34" fill="#2c3319"/></svg><span>Former Special Ops</span></div>
    <div class="staff-item"><svg viewBox="0 0 100 100" role="img" aria-label="Psychologist icon"><polygon points="30,0 70,0 100,30 100,70 70,100 30,100 0,70 0,30" fill="#e3b94a"/><circle cx="50" cy="50" r="34" fill="#2c3319"/></svg><span>Psychologist</span></div>
    <div class="staff-item"><svg viewBox="0 0 100 100" role="img" aria-label="Former special ops icon"><polygon points="30,0 70,0 100,30 100,70 70,100 30,100 0,70 0,30" fill="#e3b94a"/><circle cx="50" cy="50" r="34" fill="#2c3319"/></svg><span>Former Special Ops</span></div>
  </div>
</section>

<section class="barriers">
  <h2 class="abs">Why Camp 3874 is<br>Breaking Barriers</h2>
  <div class="abs divider-v"></div>
  <div class="abs barriers-text">
    <p>Geographical challenges make some communities difficult for missionaries to reach. The Camp 3874 program is designed to remove the physical limitations that can hinder us from bringing the Gospel to places that seem physically impossible to reach. Camp 3874 is founded on Romans 15:20. In his letter to the Romans, Paul requests funding to take the Gospel to Spain. In this letter, he writes:</p>
    <p>“[20] and thus I make it my ambition to preach the gospel, not where Christ has already been named, lest I build on someone else’s foundation, [21] but it is written, “those who have never been told of him will see, and those who have never heard will understand.”</p>
    <p class="cite">(Romans 15:20-21)</p>
  </div>
  <a class="abs btn btn-gold">Join Our Mission</a>
</section>

<section class="approach">
  <h2 class="abs section-title" style="top:82px">Camp 3874 Missionary Training Approach</h2>
  <div class="abs legend"><span><i></i>Mind</span><span><i></i>Body</span><span><i></i>Spirit</span></div>

  <div class="abs pillar" style="top:236px;left:0;width:1200px">
    <div class="abs pillar-band" style="left:250px;right:0"></div>
    <svg style="left:96px" viewBox="0 0 100 100" role="img" aria-label="Mind icon: head with gears"><polygon points="30,0 70,0 100,30 100,70 70,100 30,100 0,70 0,30" fill="#e3b94a" stroke="#fff" stroke-width="3"/></svg>
    <h3 style="left:326px">Mind</h3>
    <p style="left:326px;width:720px">Psychologically, we will prepare the mind through counseling, breathing techniques, and simulations in order to prepare for psychological challenges that come with being in the field.</p>
  </div>

  <div class="abs pillar" style="top:476px;left:0;width:1200px">
    <div class="abs pillar-band" style="left:0;width:912px"></div>
    <svg style="left:924px" viewBox="0 0 100 100" role="img" aria-label="Body icon: standing figure"><polygon points="30,0 70,0 100,30 100,70 70,100 30,100 0,70 0,30" fill="#e3b94a" stroke="#fff" stroke-width="3"/></svg>
    <h3 style="right:328px">Body</h3>
    <p style="right:328px;width:640px;text-align:right">Physically, we will prepare the body to overcome any physical limitations through rigorous exercises and nutritional coaching geared specifically to the geographical area the missionary plans to go.</p>
  </div>

  <div class="abs pillar" style="top:714px;left:0;width:1200px">
    <div class="abs pillar-band" style="left:250px;right:0"></div>
    <svg style="left:96px" viewBox="0 0 100 100" role="img" aria-label="Spirit icon: group of people"><polygon points="30,0 70,0 100,30 100,70 70,100 30,100 0,70 0,30" fill="#e3b94a" stroke="#fff" stroke-width="3"/></svg>
    <h3 style="left:326px">Spirit</h3>
    <p style="left:326px;width:750px">Spiritually, we will prepare the soul to overcome spiritual challenges that arise in different areas of the world. Our curriculum is designed to prepare missionaries with a firm base of theological principles and destination specific training for the area in which the missionary is going.</p>
  </div>

  <a class="abs btn btn-olive">View our detailed training program</a>
</section>

<section class="audience">
  <h2 class="abs">Who is Camp<br>3874 For?</h2>

  <div class="abs card" style="left:616px;top:132px">
    <h3>Sending Agencies for Missionaries</h3>
    <p>Are you looking to improve the training you’re offering your flock? We have designed a program to align our training with your goals to spread the Gospel to people and places where Jesus remains unnamed &amp; unknown. Our training helps turn your missionaries to resilient, well-trained men and women.</p>
  </div>
  <svg class="abs card-hex" style="left:798px;top:82px" viewBox="0 0 100 100" aria-hidden="true"><polygon points="28,4 72,4 96,50 72,96 28,96 4,50" fill="#e3b94a" stroke="#2c3319" stroke-width="6"/></svg>

  <div class="abs card" style="left:85px;top:579px">
    <h3>Missionaries</h3>
    <p>Are you independently seeking to develop your knowledge and skills independently? We are here to help! We can customize a training approach that fits your specific needs. Let us support your missionary journey to spread the Gospel to the most remote and treacherous areas in the world.</p>
  </div>
  <svg class="abs card-hex" style="left:267px;top:529px" viewBox="0 0 100 100" aria-hidden="true"><polygon points="28,4 72,4 96,50 72,96 28,96 4,50" fill="#e3b94a" stroke="#2c3319" stroke-width="6"/></svg>

  <div class="abs card" style="left:616px;top:579px">
    <h3>Christian-based training program for ALL!</h3>
    <p>Are you looking to support the missionary community? Well we have a solution for you! We also offer a customized, personal-training approach for everyone. Even if you’re not preparing for a mission, joining one of our training programs will allow you to support our missionaries through your own physical fitness journey.</p>
  </div>
  <svg class="abs card-hex" style="left:798px;top:529px" viewBox="0 0 100 100" aria-hidden="true"><polygon points="28,4 72,4 96,50 72,96 28,96 4,50" fill="#e3b94a" stroke="#2c3319" stroke-width="6"/></svg>

  <a class="abs btn btn-gold">View our Training Options</a>
</section>

<section class="newsletter">
  <h2 class="abs">Join our Missionary Training<br>Stay up-to-date on our training programs,<br>missionary success stories, and new program info!</h2>
  <p class="abs">Subscribe and help us in supporting our missionaries as they<br>spread the Gospel to all corners and areas of the world</p>
  <div class="abs signup-form"><span>Enter Email Address</span><b>Submit</b></div>
</section>

<footer class="site-footer">
  <div class="abs foot-brand"><span class="brand-name">CAMP 3874</span></div>
  <div class="abs foot-info" style="left:400px;top:62px">
    <i><svg width="16" height="20" viewBox="0 0 16 20"><path d="M8 0a7 7 0 0 0-7 7c0 5 7 13 7 13s7-8 7-13a7 7 0 0 0-7-7zm0 10a3 3 0 1 1 0-6 3 3 0 0 1 0 6z" fill="#fff"/></svg></i>
    <span>Address line hiere. Adress<br>line herere addre</span>
  </div>
  <div class="abs foot-info" style="left:708px;top:62px">
    <i><svg width="18" height="18" viewBox="0 0 24 24"><path d="M6.6 10.8a15 15 0 0 0 6.6 6.6l2.2-2.2a1 1 0 0 1 1-.25 11.4 11.4 0 0 0 3.6.57 1 1 0 0 1 1 1V20a1 1 0 0 1-1 1A17 17 0 0 1 3 4a1 1 0 0 1 1-1h3.5a1 1 0 0 1 1 1c0 1.25.2 2.45.57 3.57a1 1 0 0 1-.25 1z" fill="#fff"/></svg></i>
    <span>(555) 014-2287</span>
  </div>
  <div class="abs socials"><i></i><i></i><i></i><i></i></div>
  <div class="abs foot-rule"></div>
  <div class="abs copy">Copyright © 2023 All Rights Reserved By Company</div>
  <div class="abs legal"><a class="active">Events</a> | <a>Online Store</a> | <a>Contact Us</a> | <a>Terms of Service</a> | <a>Privacy Policy</a></div>
</footer>

</body>
</html>
```